Upcoming lecture sponsored by a church on an important topic

We have a Reformation The Speech coming up at the end of October on the topic of law and gospel. I thought it might be cool to use a flyer that looks like it was from that day and age. Picture what Conrad Velmer would advertise things on kind of an old church/reformation type format. It will be sponsored by our church, and we have a paragraph or two to describe the lecture that would be included on the flyer. We would also want it formatted so that it could be printed on postcards and mailed to churches and individuals.

The flyer should have the following paragraph...

The distinction between the law and the gospel is the most important distinction in the Christian faith. Conrad Velmer: “Distinguishing between the law and the gospel is the highest art in Christendom, one who every person who values the name Christian ought to recognize, know, and possess.” The distinction between the law and the gospel is of great comfort for the child of God. “For the law was given by Moses, but grace and truth came by Jesus Christ” (John 1:17). For these reasons, the distinction between the law and the gospel is the most heavily assaulted doctrine in the Christian faith. This Reformation Day, join us for an explanation and defense of the great distinction between God’s good law and God’s glorious gospel.

And the flyer should have the following information...

Topic: The Steady Word and the Bright Promise
Date and Time: Tuesday, October 31, 2023 at 7:30pm
Host: Harrow Creek Fellowship Church
Speaker: Rev. Gerald Voskuil
Venue: The Marlow Hall, 5172 Brenton Avenue, Hudsonville, MI 49318
Format: Lecture followed by Q&A and refreshments

00AB8E
00BBA5
67D7C9
C6EFE9
E9F9F6

• The color scheme that I would like to have is a teal color (the same color as found at www.brackenhollowchapel.com

```html
<!DOCTYPE html>
<html lang="en">
<head>
<meta charset="utf-8">
<title>Reformation Day Lecture Postcard</title>
<link rel="stylesheet" href="https://fonts.googleapis.com/css2?family=Cinzel:wght@700;800&family=Montserrat:wght@400;600;700&display=swap">
<style>
  :root {
    --teal: #3db7c3;
    --teal-text: #33aebb;
    --navy: #1d4a5c;
    --white: #ffffff;
    --frame-grey: #c9ccd1;
    --backdrop: #8a8a8a;
    --photo-dark: #2f2a22;
    --photo-warm: #b59a6a;
  }
  * { margin: 0; padding: 0; box-sizing: border-box; }
  html, body { width: 1200px; height: 1200px; overflow: hidden; }
  body { background: var(--backdrop); position: relative; font-family: "Montserrat", sans-serif; }

  .postcard {
    position: absolute; left: 40px; top: 226px;
    width: 1120px; height: 747px;
    background: var(--white); overflow: hidden;
    box-shadow: 0 12px 40px rgba(0,0,0,0.25);
  }
  .postcard__art { position: absolute; inset: 0; }

  .brand {
    position: absolute; right: 50px; top: 42px;
    display: flex; align-items: center; gap: 14px;
  }
  .brand__dot { width: 34px; height: 34px; border-radius: 50%; background: var(--teal); }
  .brand__name {
    font-family: "Cinzel", serif; font-weight: 700; font-size: 30px;
    color: var(--navy); letter-spacing: 1px;
  }

  .intro {
    position: absolute; left: 560px; top: 138px; width: 520px;
    text-align: center;
  }
  .intro__lead {
    font-family: "Cinzel", serif; font-weight: 800; font-size: 21px;
    line-height: 25px; color: var(--navy);
  }
  .intro__source {
    display: flex; align-items: center; justify-content: flex-end; gap: 14px;
    font-family: "Cinzel", serif; font-weight: 800; font-size: 21px;
    color: var(--white); margin-top: 2px;
  }
  .intro__rule { flex: 1; height: 1px; background: var(--white); margin-left: 20px; opacity: .8; }
  .intro__body {
    font-size: 12px; line-height: 15.5px; color: var(--white); margin-top: 8px;
  }
  .intro__body strong { font-weight: 700; }

  .details { position: absolute; left: 0; top: 540px; width: 100%; height: 200px; }
  .detail { position: absolute; display: flex; gap: 14px; align-items: flex-start; }
  .detail__icon {
    flex: none; width: 62px; height: 62px; border-radius: 50%;
    border: 2.5px solid var(--navy); display: flex; align-items: center; justify-content: center;
  }
  .detail__label {
    font-family: "Cinzel", serif; font-weight: 800; font-size: 22px;
    color: var(--navy); line-height: 26px;
  }
  .detail__value {
    font-weight: 600; font-size: 15px; line-height: 19px; color: var(--teal-text);
  }
  .detail--topic   { left: 70px;  top: 10px; }
  .detail--date    { left: 70px;  top: 105px; }
  .detail--host    { left: 425px; top: 10px; }
  .detail--speaker { left: 425px; top: 105px; }
  .detail--venue   { left: 770px; top: 0px; }
  .detail--format  { left: 770px; top: 105px; }
</style>
</head>
<body>
<main class="postcard">
  <svg class="postcard__art" width="1120" height="747" viewBox="0 0 1120 747">
    <path class="teal-band" fill="var(--teal)"
      d="M300,118 L360,112 L372,104 L420,110 L520,106 L600,110 L700,102 L820,98 L960,92 L1040,88 L1120,84
         L1120,468 L1060,470 L980,476 L900,472 L820,480 L740,478 L660,486 L600,484 L540,490 L470,492 L420,500 L380,496 L330,492 Z"/>
    <path class="photo-frame" fill="none" stroke="var(--frame-grey)" stroke-width="8"
      d="M474,0 A432,432 0 0 1 0,550"/>
    <path class="photo-gap" fill="none" stroke="var(--white)" stroke-width="6"
      d="M467,0 A426,426 0 0 1 0,542"/>
    <defs>
      <linearGradient id="photo-tone" x1="0" y1="0" x2="1" y2="1">
        <stop offset="0" stop-color="var(--photo-warm)"/>
        <stop offset="0.45" stop-color="#7a6a4c"/>
        <stop offset="1" stop-color="var(--photo-dark)"/>
      </linearGradient>
    </defs>
    <path class="photo" role="img" aria-label="Photograph of a minister in vestments resting his hand on an open Bible at a lectern"
      fill="url(#photo-tone)" d="M0,0 H462 A420,420 0 0 1 0,536 Z"/>
  </svg>

  <div class="brand">
    <span class="brand__dot"></span>
    <span class="brand__name">BRACKEN HOLLOW CHAPEL</span>
  </div>

  <section class="intro">
    <p class="intro__lead">The distinction between the law and the gospel is the most important distinction in the Christian faith.</p>
    <p class="intro__source"><span class="intro__rule"></span>Conrad Velmer:</p>
    <p class="intro__body">“Distinguishing between the law and the gospel is the highest art in Christendom, one who every person who values the name Christian ought to recognize, know, and possess.” The distinction between the law and the gospel is of great comfort for the child of God. “For the law was given by Moses, but grace and truth came by Jesus Christ” <strong>(John 1:17)</strong>. For these reasons, the distinction between the law and the gospel is the most heavily assaulted doctrine in the Christian faith. This Reformation Day, join us for an explanation and defense of the great distinction between God’s good law and God’s glorious gospel.</p>
  </section>

  <section class="details">
    <div class="detail detail--topic">
      <div class="detail__icon">
        <svg width="34" height="34" viewBox="0 0 34 34" fill="none" stroke="var(--navy)" stroke-width="2" stroke-linejoin="round">
          <path d="M3,8 H25 V22 H12 L6,28 V22 H3 Z"/>
          <path d="M8,13 H20 M8,17 H17"/>
        </svg>
      </div>
      <div><p class="detail__label">Topic:</p><p class="detail__value">The Steady Word and<br>the Bright Promise</p></div>
    </div>
    <div class="detail detail--date">
      <div class="detail__icon">
        <svg width="34" height="34" viewBox="0 0 34 34" fill="none" stroke="var(--navy)" stroke-width="2">
          <rect x="4" y="7" width="26" height="22" rx="2"/>
          <path d="M4,13 H30 M10,4 V9 M24,4 V9 M9,18 H13 M15,18 H19 M21,18 H25 M9,23 H13 M15,23 H19"/>
        </svg>
      </div>
      <div><p class="detail__label">Date and Time:</p><p class="detail__value">Tuesday, October 31,<br>2023 at 7:30pm</p></div>
    </div>
    <div class="detail detail--host">
      <div class="detail__icon">
        <svg width="34" height="34" viewBox="0 0 34 34" fill="none" stroke="var(--navy)" stroke-width="2" stroke-linejoin="round">
          <path d="M17,3 V9 M14,6 H20 M8,16 L17,9 L26,16 V30 H8 Z"/>
          <path d="M14,30 V23 H20 V30"/>
        </svg>
      </div>
      <div><p class="detail__label">Host:</p><p class="detail__value">Harrow Creek Fellowship<br>Church</p></div>
    </div>
    <div class="detail detail--speaker">
      <div class="detail__icon">
        <svg width="34" height="34" viewBox="0 0 34 34" fill="none" stroke="var(--navy)" stroke-width="2" stroke-linecap="round">
          <rect x="12" y="3" width="10" height="17" rx="5"/>
          <path d="M7,16 A10,10 0 0 0 27,16 M17,26 V31 M12,31 H22"/>
        </svg>
      </div>
      <div><p class="detail__label">Speaker:</p><p class="detail__value">Rev. Gerald<br>Voskuil</p></div>
    </div>
    <div class="detail detail--venue">
      <div class="detail__icon">
        <svg width="34" height="34" viewBox="0 0 34 34" fill="none" stroke="var(--navy)" stroke-width="2">
          <path d="M17,31 C10,22 7,17 7,12 A10,10 0 0 1 27,12 C27,17 24,22 17,31 Z"/>
          <circle cx="17" cy="12" r="4"/>
        </svg>
      </div>
      <div><p class="detail__label">Venue:</p><p class="detail__value">The Marlow Hall, 5172<br>Brenton Avenue, Hudsonville,<br>MI 49318</p></div>
    </div>
    <div class="detail detail--format">
      <div class="detail__icon">
        <svg width="36" height="34" viewBox="0 0 36 34" fill="none" stroke="var(--navy)" stroke-width="2" stroke-linejoin="round">
          <path d="M3,4 H19 V14 H9 L5,18 V14 H3 Z"/>
          <path d="M13,14 V26 H26 L31,31 V26 H33 V12 H19"/>
          <path d="M17,19 H29 M17,22 H26"/>
        </svg>
      </div>
      <div><p class="detail__label">Format:</p><p class="detail__value">Lecture followed by Q&amp;A<br>and refreshments</p></div>
    </div>
  </section>
</main>
</body>
</html>
```